Training Course Info Brochure

Hi there, I'm looking for a design for A4 Flyer (2-3 pages) on our new Course - Infection Control. I have included a previous brochure on our courses so the designed can see the look and feel we are looking for.

As this is about Infection Control, I would also like to see some RED in the design or wording.

The brochure will need to include quite a few industry/ government logos as well and graphics are important. I have included some (Health Care Industry workers) and am also open to other graphics.

Thanks for considering!

Target Market(s)

The Health profession and students wanting to work in the health field

Industry/Entity Type

Health Care

Font styles to use
Sans Serif

Colors
3277b5
f78f20
ffffff
ec1f27

Requirements
Must have
• Similar feel to the brochure I have included in this brief.

SOME RED lettering as we are teaching Infection Control during the COVID19 pandemic
Nice to have
• Lovely design with quite a few photos graphics

Company details:

Carrow Academy of Learning
RTO 73648
FREECALL : 1800 437 982
www.carrowlearning.edu.au
info@carrowlearning.edu.au

```html
<!DOCTYPE html>
<html lang="en">
<head>
<meta charset="utf-8">
<title>Infection Control Course Brochure – Carrow Academy of Learning</title>
<link rel="stylesheet" href="https://fonts.googleapis.com/css2?family=Roboto+Slab:wght@800&family=Roboto+Condensed:wght@400;500&family=Montserrat:wght@400;500&display=swap">
<style>
  :root{
    --blue:#3277b5;
    --navy:#1f5a8f;
    --panel:#255f95;
    --orange:#f78f20;
    --red:#ec1f27;
    --white:#ffffff;
    --ink:#2b2b2b;
    --paper:#ffffff;
    --backdrop:#e9eaec;
    --rule:#222222;
  }
  *{box-sizing:border-box;margin:0;padding:0}
  html,body{width:1200px;height:907px;overflow:hidden;background:var(--backdrop)}
  .spread{position:relative;width:1200px;height:907px}
  .page{position:absolute;top:62px;width:540px;height:780px;background:var(--paper)}
  .page--left{left:60px;box-shadow:inset -18px 0 24px -20px rgba(0,0,0,.25)}
  .page--right{left:600px;box-shadow:inset 18px 0 24px -20px rgba(0,0,0,.2)}

  .page-title{position:absolute;font-family:"Roboto Slab",Georgia,serif;font-weight:800;font-size:27px;line-height:1;color:var(--navy);letter-spacing:-.2px}
  .page-title .accent{color:var(--orange)}
  .title-rule{position:absolute;height:2px;background:var(--rule)}
  .subtitle{position:absolute;font-family:"Roboto Condensed",Arial,sans-serif;font-weight:500;font-size:17px;color:var(--red);white-space:nowrap}

  .photo{position:absolute}
  .photo--carer{left:23px;top:145px;width:467px;height:308px;background:linear-gradient(120deg,#c9d6dc 0%,#e9e5e0 45%,#f2ece6 70%,#d9dde2 100%)}
  .photo--clinic{left:266px;top:198px;width:274px;height:224px;background:linear-gradient(110deg,#cfd9e1 0%,#e3e9ee 45%,#bfe0df 75%,#e7ecef 100%)}
  .photo--gloves{left:12px;top:373px;width:236px;height:222px;background:radial-gradient(circle at 50% 55%,#8fc6ef 0%,#b9d9ef 35%,#eef1f4 75%)}

  .info-panel{position:absolute;background:var(--panel);color:var(--white);font-family:Montserrat,Arial,sans-serif}
  .info-panel--about{left:68px;top:403px;width:472px;height:315px;padding:38px 16px 0 18px;font-size:10.3px;line-height:1.36}
  .info-panel--about p{margin-bottom:11px}

  .body-copy{position:absolute;font-family:Montserrat,Arial,sans-serif;font-size:10.6px;line-height:1.38;color:var(--ink)}
  .body-copy p{margin-bottom:12px}

  .panel-heading{font-family:"Roboto Condensed",Arial,sans-serif;font-weight:500;font-size:17px;line-height:1.3;color:var(--orange)}

  .recognised-band{position:absolute;left:0;top:595px;width:495px;height:123px;background:var(--panel);padding:13px 18px 0 20px;color:var(--white);font-family:Montserrat,Arial,sans-serif;font-size:10.4px;line-height:1.35}
  .recognised-band .panel-heading{margin-bottom:9px}
  .mentor-block{position:absolute;left:248px;top:422px;width:247px;height:174px;background:var(--panel);padding:15px 14px 0 20px;color:var(--white);font-family:Montserrat,Arial,sans-serif;font-size:10.3px;line-height:1.3}
  .mentor-block .panel-heading{margin-bottom:11px}

  .page-number{position:absolute;width:27px;height:27px;border:1.5px solid #333;font-family:Montserrat,Arial,sans-serif;font-weight:500;font-size:13px;color:#333;display:flex;align-items:center;justify-content:center}
</style>
</head>
<body>
<main class="spread">

  <section class="page page--left">
    <h1 class="page-title" style="left:48px;top:44px">About <span class="accent">This Course</span></h1>
    <div class="title-rule" style="left:48px;top:84px;width:472px"></div>
    <p class="subtitle" style="left:48px;top:92px">Protect yourself and others in the community from infectious diseases</p>

    <div class="photo photo--carer" role="img" aria-label="Photo of a smiling nurse handing a glass of water to an elderly woman"></div>

    <div class="info-panel info-panel--about">
      <p>There is not better time than now, to formally Upskill yourself and your team with a Nationally Accredited unit of Competency in Infection Control prevention including the latest COVID19 infection control protocols (Department of Health). Fast track your skills with Carrow's Accredited Infection Control Skill set to get you job ready or enhance your current workplace skills.</p>
      <p>The COVID19 pandemic has highlighted the important of building the capacity and understanding of the workforce to practice safe infection control procedures.</p>
      <p>This skill set will provide you with the skills and knowledge to assist inprotecting yourself and others in the community from infectious diseases.</p>
      <p>You will understand how infections are spread, ways of preventing the spread of infection and how to protect yourselfand others from infection.</p>
      <p>The skill set is becoming increasingly important for all Health Care Workers – and all workers are encouraged to upskill themselves today, whether you are becoming Job Ready or for your professional development in Industry.</p>
    </div>

    <div class="page-number" style="left:46px;top:738px">2</div>
  </section>

  <section class="page page--right">
    <h1 class="page-title" style="left:18px;top:54px">Course <span class="accent">Format -</span></h1>
    <div class="title-rule" style="left:18px;top:89px;width:490px"></div>
    <p class="subtitle" style="left:18px;top:98px">Online with face-to-face tutorial (in person or via MeetSpace)</p>

    <div class="body-copy" style="left:20px;top:152px;width:480px">
      <p>Our course is delivered to you online which allows you to undertaken study at your own pace. It is recommended completion occurs within a month.</p>
    </div>
    <div class="body-copy" style="left:20px;top:195px;width:236px">
      <p>you have completed the Online Component of your course, you are invited into a Practical Lab Session via face to face learning; to practice skills and undertake a workplace simulated activity.</p>
      <p>Regional locations may be fulfilled by MeetSpace technology and Carrow may also conduct on-site visits as required. Carrow also travel to regional locations throughout the year. Group training sessions are also available for corporates and workplaces.</p>
    </div>

    <div class="photo photo--clinic" role="img" aria-label="Photo of a nurse in a clinic using hand sanitiser, a doctor in the background"></div>

    <div class="mentor-block">
      <h2 class="panel-heading">Mentor Support and<br>Practical Sessions</h2>
      <p>Students are welcomed to the course by a short induction by your Tutor/ Mentor to start you on your way with confidence! All of Carrow's student resources, learner materials, videos are contained in Carrow's easy to use LMS and learning is provided online at your convenience.</p>
    </div>

    <div class="recognised-band">
      <h2 class="panel-heading">Industry Recognised</h2>
      <p>Carrow's unique program in Infection Control is supported by leading Industry bodies, and includes certification by the Department of Health, and other leading Health bodies in Australia. Our Unit of competency is Australian Recognised and Accredited.</p>
    </div>

    <div class="photo photo--gloves" role="img" aria-label="Photo of two hands in blue medical gloves forming a heart shape"></div>

    <div class="page-number" style="left:493px;top:733px">3</div>
  </section>

</main>
</body>
</html>
```